Webdesign für Management Coaching
Zielgruppe
Ich bin Coach/biete Coaching-Leistungen an.
Zielgruppe: Fokus auf Führungskräfte/Entscheider/Management mit technischem Hintergrund (Forschung & Entwicklung, Engineering, Technik, Maschinenbau, Naturwissenschaften)
Coaching-Schwerpunkte: Sinn-Coaching, Begleitung bei Umbrüchen und Veränderungen (privat & beruflich), Sparring & Reflexion
Aufgabenstellung
Gewünscht wurde ein helles Design, das die Logo-Farben aufnimmt. Ausrichtung am Logo & den verwendeten Farben, Schriften
Bilder: Ich werde noch Fotos beim Fotografen machen, die eingebunden werden sollen (Profil, etc.). Bitte Anhaltspunkte nennen, worauf ich die Fotografin hinweisen soll/welche Motive ins Konzept passen.

```html
<!DOCTYPE html>
<html lang="de">
<head>
<meta charset="utf-8">
<title>Weitblick Coaching – Sinn-Coaching für Führungskräfte</title>
<link href="https://fonts.googleapis.com/css2?family=Libre+Baskerville:wght@400;700&family=Great+Vibes&family=Roboto:wght@300;400;500&display=swap" rel="stylesheet">
<style>
  :root {
    --page: #f7f7f7;
    --white: #ffffff;
    --teal: #92d0cf;
    --blue: #8db4cc;
    --blue-dark: #6f8ea6;
    --orange: #f2b13a;
    --slate: #6f8194;
    --text: #5b6d7e;
    --text-soft: #8a98a6;
    --line: #e3e7ea;
    --serif: "Libre Baskerville", Georgia, serif;
    --script: "Great Vibes", cursive;
    --sans: "Roboto", Arial, sans-serif;
  }
  * { box-sizing: border-box; margin: 0; padding: 0; }
  html, body { width: 1000px; height: 1200px; overflow: hidden; background: var(--page); }
  body { font-family: var(--serif); color: var(--text); }
  .page { width: 1000px; height: 1200px; position: relative; overflow: hidden; background: var(--page); }

  /* header */
  .site-header { height: 34px; background: var(--white); border-bottom: 1px solid var(--line); display: flex; align-items: center; position: relative; }
  .brand-small { display: flex; align-items: center; gap: 6px; padding-left: 14px; font-family: var(--serif); font-size: 10px; letter-spacing: 1.5px; color: var(--blue-dark); text-transform: uppercase; }
  .brand-dot { width: 8px; height: 8px; border-radius: 50%; background: var(--blue); }
  .main-nav { position: absolute; left: 50%; transform: translateX(-50%); display: flex; gap: 16px; font-size: 9px; color: var(--text); }
  .nav-cta { position: absolute; right: 0; top: 0; height: 34px; width: 80px; background: var(--blue); color: var(--white); font-family: var(--sans); font-size: 8px; letter-spacing: 1px; display: flex; align-items: center; justify-content: center; }

  /* hero */
  .hero { position: relative; height: 300px; }
  .hero-photo { position: absolute; inset: 0; background: linear-gradient(100deg, #f3f2f4 0%, #ecebee 35%, #cfc2c6 55%, #b9a79e 68%, #f4d9a4 88%, #fbe8b8 100%); }
  .hero-wave { position: absolute; left: 0; bottom: -1px; width: 1000px; height: 40px; }
  .hero-brand { position: absolute; left: 70px; top: 70px; width: 300px; text-align: center; }
  .hero-brand .brand-circle { width: 100px; height: 100px; border: 1px solid var(--blue); border-radius: 50%; margin: 0 auto 22px; }
  .hero-brand .brand-name { font-family: var(--serif); font-size: 18px; letter-spacing: 3px; color: var(--blue-dark); text-transform: uppercase; }

  /* intro */
  .intro { text-align: center; padding: 22px 0 0; height: 150px; }
  .intro-kicker { font-size: 19px; letter-spacing: 3px; color: var(--text); }
  .intro-script { font-family: var(--script); font-size: 42px; color: var(--blue); line-height: 1.05; }
  .intro-sub { font-size: 16px; letter-spacing: 2.5px; color: var(--text); }
  .intro-lead { font-size: 10px; line-height: 1.7; margin-top: 10px; color: var(--text); }

  /* coach band */
  .coach { position: relative; margin: 0 70px; height: 170px; display: flex; }
  .coach-text { flex: 1; background: var(--teal); padding: 16px 26px; color: var(--white); }
  .coach-title { font-family: var(--sans); font-weight: 300; font-size: 22px; }
  .coach-script { font-family: var(--script); font-size: 26px; line-height: 1; margin-bottom: 10px; }
  .coach-copy { font-size: 8px; line-height: 1.7; max-width: 420px; }
  .btn { display: inline-block; font-family: var(--serif); font-size: 7.5px; color: var(--white); padding: 5px 18px; text-transform: uppercase; letter-spacing: .5px; }
  .btn-orange { background: var(--orange); }
  .btn-blue { background: var(--blue); }
  .coach-actions { margin-top: 10px; display: flex; gap: 10px; }
  .coach-photo { width: 300px; background: linear-gradient(120deg, var(--teal) 0%, #bfe2e1 45%, #e9eef0 100%); }

  /* focus cards */
  .focus { display: flex; gap: 16px; margin: 14px 70px 0; }
  .focus-card { flex: 1; background: var(--white); padding: 14px 14px 12px; box-shadow: 0 2px 10px rgba(90,110,130,.08); }
  .focus-icon { width: 30px; height: 30px; border-radius: 50%; background: #e5eef3; }
  .focus-title { font-family: var(--script); font-size: 22px; color: var(--orange); margin: 6px 0 4px; }
  .focus-copy { font-size: 7.5px; line-height: 1.75; color: var(--text); }

  /* choice */
  .choice { display: grid; grid-template-columns: 1fr 1fr 1fr; grid-template-rows: 90px 90px; margin: 20px 70px 0; background: var(--white); }
  .choice-photo { width: 100%; height: 100%; }
  .photo-meeting { background: linear-gradient(135deg, #9aa3ab, #c9ced2 50%, #6f7882); }
  .photo-online { background: linear-gradient(135deg, #c8c3bc, #8d8f92 55%, #434a55); }
  .photo-coach { background: linear-gradient(180deg, #f2f2f2, #e4e4e6); }
  .choice-head { display: flex; align-items: center; justify-content: center; font-family: var(--script); font-size: 26px; color: var(--slate); }
  .choice-offer { text-align: center; padding-top: 22px; }
  .choice-offer h3 { font-family: var(--serif); font-weight: 400; font-size: 12px; letter-spacing: 1px; color: var(--text); margin-bottom: 8px; }
  .choice-offer .btn { text-transform: none; font-weight: 700; }

  /* booking */
  .booking { display: flex; align-items: center; margin: 20px 70px 0; gap: 40px; }
  .booking-intro { flex: 1; }
  .booking-kicker { font-family: var(--sans); font-weight: 300; font-size: 17px; color: var(--slate); }
  .booking-script { font-family: var(--script); font-size: 30px; color: var(--orange); line-height: 1.1; border-bottom: 1px solid var(--line); padding-bottom: 4px; width: 260px; }
  .booking-copy { font-size: 8px; line-height: 1.8; margin-top: 8px; color: var(--text); }
  .booking-widget { width: 400px; height: 190px; display: flex; background: var(--white); box-shadow: 0 4px 16px rgba(80,100,120,.15); font-family: var(--sans); }
  .widget-nav { width: 120px; background: var(--slate); color: var(--white); padding: 8px 6px; font-size: 7.5px; display: flex; flex-direction: column; }
  .widget-step { padding: 6px 8px; border-radius: 2px; display: flex; justify-content: space-between; align-items: center; }
  .widget-step.is-active { background: rgba(255,255,255,.12); }
  .step-ring { width: 9px; height: 9px; border-radius: 50%; border: 1.5px solid rgba(255,255,255,.8); }
  .widget-collapse { margin-top: auto; padding: 6px 8px; display: flex; justify-content: space-between; border-top: 1px solid rgba(255,255,255,.15); }
  .widget-main { flex: 1; display: flex; flex-direction: column; font-size: 8px; color: var(--text); }
  .widget-head { padding: 10px 14px; border-bottom: 1px solid var(--line); font-size: 9px; }
  .widget-body { padding: 10px 14px; flex: 1; }
  .widget-label { font-size: 7px; margin-bottom: 4px; }
  .widget-label span { color: var(--orange); }
  .widget-select { border: 1px solid var(--blue); height: 18px; padding: 0 6px; display: flex; align-items: center; justify-content: space-between; color: #b6c0c8; font-size: 7px; }
  .widget-options { margin-top: 6px; font-size: 7px; }
  .widget-options li { list-style: none; padding: 4px 4px; }
  .widget-options li.is-hover { background: #f1f3f5; }
  .widget-foot { border-top: 1px solid var(--line); padding: 6px 14px; display: flex; justify-content: flex-end; }
  .widget-next { background: var(--blue); color: var(--white); font-size: 7px; padding: 4px 12px; border-radius: 2px; }
</style>
</head>
<body>
<div class="page">

  <header class="site-header">
    <div class="brand-small"><span class="brand-dot"></span>Weitblick Coaching</div>
    <nav class="main-nav">
      <span>Leistungen</span><span>Über mich</span><span>Coaching</span><span>Buchen</span><span>Kundenstimmen</span><span>Blog</span><span>Kontakt</span>
    </nav>
    <div class="nav-cta">KONTAKT</div>
  </header>

  <section class="hero">
    <div class="hero-photo" role="img" aria-label="Foto: Frau sitzt auf einem Felsen und blickt in eine weite Berglandschaft im warmen Gegenlicht"></div>
    <svg class="hero-wave" viewBox="0 0 1000 40" preserveAspectRatio="none" aria-hidden="true">
      <path d="M0 22 C 250 40, 500 0, 1000 24 L1000 40 L0 40 Z" fill="#f7f7f7"/>
    </svg>
    <div class="hero-brand">
      <div class="brand-circle"></div>
      <div class="brand-name">Weitblick Coaching</div>
    </div>
  </section>

  <section class="intro">
    <h1 class="intro-kicker">Meistern Sie den Wandel:</h1>
    <div class="intro-script">Sinn-Coaching</div>
    <div class="intro-sub">für Führungskräfte</div>
    <p class="intro-lead">Begleitung bei beruflichen und privaten Umbrüchen –<br>Ihr Wegbegleiter für nachhaltige Entwicklung und Reflexion.</p>
  </section>

  <section class="coach">
    <div class="coach-text">
      <h2 class="coach-title">Ihr Coach</h2>
      <div class="coach-script">für den Wandel</div>
      <p class="coach-copy">Hallo, mein Name ist Tobias, und ich bin Ihr Coach für Sinnfindung und Entwicklung. Mit einem tiefen Verständnis für die Herausforderungen, denen Führungskräfte in technischen und innovativen Bereichen gegenüberstehen, begleite ich Sie durch berufliche und private Veränderungen. Gemeinsam entdecken wir Ihre wahren Ziele, stärken Ihre Resilienz und entwickeln Strategien, die Ihre Führungsqualitäten verbessern. Ich freue mich darauf, Sie auf Ihrer Reise zu begleiten.</p>
      <div class="coach-actions"><span class="btn btn-orange">Kontakt</span><span class="btn btn-blue">Mehr erfahren</span></div>
    </div>
    <div class="coach-photo" role="img" aria-label="Porträtfoto: Coach im weißen Hemd, Hände in den Hüften"></div>
  </section>

  <section class="focus">
    <article class="focus-card">
      <div class="focus-icon" role="img" aria-label="Icon: Kopf mit Gedanken"></div>
      <h3 class="focus-title">Sinn-Coaching</h3>
      <p class="focus-copy">Sinn-Coaching hilft Ihnen, Ihre tiefsten Werte und Überzeugungen zu entdecken und mit Ihrem beruflichen und privaten Leben in Einklang zu bringen. So gewinnen Sie Klarheit über Ihre Ziele und stärken Ihre Motivation.</p>
    </article>
    <article class="focus-card">
      <div class="focus-icon" role="img" aria-label="Icon: Person im Wandel"></div>
      <h3 class="focus-title">Umbrüche &amp; Veränderungen</h3>
      <p class="focus-copy">Veränderungen sind ein natürlicher Teil des Lebens und der Karriere. Ich unterstütze Sie dabei, Übergänge sicher zu gestalten, Widerstandsfähigkeit zu entwickeln und Veränderungen als Chance für Wachstum zu sehen.</p>
    </article>
    <article class="focus-card">
      <div class="focus-icon" role="img" aria-label="Icon: zwei Personen im Austausch"></div>
      <h3 class="focus-title">Sparring &amp; Reflexion</h3>
      <p class="focus-copy">Ich biete Ihnen einen geschützten Raum, in dem Sie Ihre Gedanken offenlegen und kritisch prüfen können. Als Sparringspartner helfe ich Ihnen, Lösungsansätze zu finden und Ihre Entscheidungskompetenz zu steigern.</p>
    </article>
  </section>

  <section class="choice">
    <div class="choice-photo photo-meeting" role="img" aria-label="Foto: Coaching-Gespräch im Freien auf einer Treppe"></div>
    <div class="choice-head">Sie haben die Wahl!</div>
    <div class="choice-photo photo-online" role="img" aria-label="Foto: Coach mit Headset im Online-Gespräch am Laptop"></div>
    <div class="choice-offer"><h3>PERSÖNLICHES COACHING</h3><span class="btn btn-orange">Mehr erfahren</span></div>
    <div class="choice-photo photo-coach" role="img" aria-label="Foto: Coach zeigt mit beiden Händen nach links und rechts"></div>
    <div class="choice-offer"><h3>ONLINE COACHING</h3><span class="btn btn-orange">Mehr erfahren</span></div>
  </section>

  <section class="booking">
    <div class="booking-intro">
      <h2 class="booking-kicker">Bereit für das Erstgespräch?</h2>
      <div class="booking-script">Jetzt Online buchen</div>
      <p class="booking-copy">Bevor das Coaching beginnt, lerne ich Sie gerne vorher kennen, um Ihnen mein Konzept näher zu bringen und mir ein Bild von Ihnen zu machen.</p>
    </div>
    <div class="booking-widget">
      <div class="widget-nav">
        <div class="widget-step is-active">Dienstleistung <span class="step-ring"></span></div>
        <div class="widget-step">Datum &amp; Uhrzeit</div>
        <div class="widget-step">Kontaktinformation</div>
        <div class="widget-collapse">Collapse menu <span>›</span></div>
      </div>
      <div class="widget-main">
        <div class="widget-head">Dienstleistung</div>
        <div class="widget-body">
          <div class="widget-label"><span>*</span> Dienstleistung:</div>
          <div class="widget-select">Dienstleistung auswählen <span>˄</span></div>
          <ul class="widget-options">
            <li>Coaching per Mail</li>
            <li>Lebenscoaching</li>
            <li class="is-hover">Schreibworkshop</li>
          </ul>
        </div>
        <div class="widget-foot"><span class="widget-next">Weiter</span></div>
      </div>
    </div>
  </section>

</div>
</body>
</html>
```